Vindmark Health & Wellness needs a fresh and interesting website

I need a rebrand and redevelopment of my website, www.dellaquorne.example
Our mission is provide bespoke , lifestyle medicine , everyone has their own path to health. and we are creating a personalized experience for people to life their life to the fullest
Vindmark - means sea lands
I need an landing page and about page and potentially a few project launch pages , I have been using Wordpress for my basic information and then I use Plovix for the launch pages of my programs since I can edit those easily.

Target Market(s)

Corporate and individual's who are interested in a different perspective on health and wellness , and living with a chronic illness

Industry/Entity Type

Health, lifestyle , wellness coaching and medicine

Coding

Number of Pages Required

Font styles to use
Other font styles liked:
• look into the logo

Requirements
Must have
• the logo I uploaded
Nice to have
• I want a fresh perspective on health, I have bamboo, hibiscus vibes in my logo , but also like more of a water vibe/ I want something earthy but not too boho it needs to be clean
Should not have
• every other holistic health vibe,

```html
<!DOCTYPE html>
<html lang="en">
<head>
<meta charset="utf-8">
<title>Vindmark Health &amp; Wellness</title>
<link rel="stylesheet" href="https://fonts.googleapis.com/css2?family=Poppins:wght@400;500;600;700;800&family=Lato:wght@400;700&display=swap">
<style>
:root{
  --blue-deep:#0b6590;
  --blue-light:#1fa3cc;
  --green:#66b512;
  --ink:#2b2b2b;
  --footer-bg:#061a1c;
  --soft-bg:#f4f4f4;
  --white:#ffffff;
}
*{box-sizing:border-box;margin:0;padding:0}
html,body{width:1200px;height:2743px;overflow:hidden;background:var(--white)}
body{font-family:"Lato",sans-serif;color:var(--ink)}
.page{position:relative;width:1200px;height:2743px;overflow:hidden}
.abs{position:absolute}

/* hero */
.hero{left:0;top:0;width:1200px;height:728px;
  background:
    radial-gradient(ellipse 150px 260px at 830px 420px,rgba(196,160,110,.55) 0%,rgba(120,110,90,.35) 45%,transparent 75%),
    radial-gradient(ellipse 260px 90px at 830px 650px,#56613e 0%,#3d4a30 50%,transparent 85%),
    radial-gradient(ellipse 220px 70px at 120px 600px,#3e4c32 0%,transparent 80%),
    radial-gradient(ellipse 200px 60px at 480px 560px,#35432d 0%,transparent 80%),
    radial-gradient(ellipse 700px 180px at 600px 90px,#173f24 0%,transparent 80%),
    linear-gradient(180deg,#0f2c1b 0%,#1a3a25 28%,#24372d 48%,#2f3a33 66%,#3a4536 84%,#47503d 100%)}
.hero-shade{left:0;top:0;width:1200px;height:728px;background:linear-gradient(90deg,rgba(0,0,0,.35) 0%,rgba(0,0,0,.1) 55%,transparent 100%)}
.nav{font-family:"Poppins",sans-serif;font-weight:600;font-size:13px;color:var(--white);letter-spacing:.2px}
.nav-line{height:1px;background:rgba(255,255,255,.75)}
.nav-home{left:112px;top:36px;width:70px;height:36px;border:2px solid var(--blue-light);display:flex;align-items:center;justify-content:center}
.brand{font-family:"Poppins",sans-serif;font-weight:500;color:var(--white);display:flex;align-items:center;gap:10px}
.brand-dot{width:14px;height:14px;border-radius:50%;background:var(--white)}
.hero-title{left:110px;top:282px;font-family:"Poppins",sans-serif;font-weight:700;font-size:84px;color:var(--white);letter-spacing:1px;line-height:1}
.hero-text{left:112px;top:402px;width:450px;font-size:15.5px;line-height:26px;color:var(--white)}
.btn{font-family:"Poppins",sans-serif;font-weight:700;font-size:15px;color:var(--white);background:var(--green);display:flex;align-items:center;justify-content:center;border-radius:3px}
.dot{width:11px;height:11px;border-radius:50%;background:var(--white);top:663px}

/* headings */
.h-strong{font-family:"Poppins",sans-serif;font-weight:800;color:var(--blue-deep)}
.h-light{font-family:"Poppins",sans-serif;font-weight:400;color:var(--blue-light)}
.h-mark{display:inline-block;width:22px;height:22px;border-radius:50%;border:2px solid var(--blue-light);vertical-align:middle;margin-left:10px}
.body-text{font-size:15.5px;line-height:25.7px;color:#3a3a3a}

/* project */
.project{left:0;top:1309px;width:1200px;height:557px;background:var(--soft-bg);overflow:hidden}

/* newsletter */
.newsletter{left:0;top:1866px;width:1200px;height:517px;
  background:
    radial-gradient(ellipse 200px 150px at 200px 400px,rgba(173,214,230,.55) 0%,transparent 80%),
    radial-gradient(ellipse 200px 150px at 1000px 400px,rgba(173,214,230,.55) 0%,transparent 80%),
    radial-gradient(ellipse 160px 220px at 120px 250px,rgba(214,228,190,.5) 0%,transparent 80%),
    radial-gradient(ellipse 160px 220px at 1080px 250px,rgba(214,228,190,.5) 0%,transparent 80%),
    #fbfcfb}
.email{left:365px;top:2151px;width:470px;height:51px;border-radius:26px;background:var(--white);box-shadow:0 2px 8px rgba(0,0,0,.08);display:flex;align-items:center;justify-content:center;font-size:15px;color:#8a8a8a}

/* footer */
.footer{left:0;top:2383px;width:1200px;height:360px;background:var(--footer-bg)}
.f-head{font-family:"Poppins",sans-serif;font-weight:500;font-size:16px;color:var(--white)}
.f-rule{width:64px;height:2px;background:var(--green)}
.f-text{font-family:"Poppins",sans-serif;font-size:15px;color:var(--white);line-height:28px}
.social{width:52px;height:52px;border-radius:50%;border:2px solid var(--green);top:2625px;display:flex;align-items:center;justify-content:center}
.social-dot{width:16px;height:16px;border-radius:50%;background:var(--white)}
.quick{list-style:none}
</style>
</head>
<body>
<div class="page">

  <!-- hero -->
  <section class="abs hero" role="img" aria-label="Woman meditating cross-legged on a mossy rock in a forest stream"></section>
  <div class="abs hero-shade"></div>

  <div class="abs nav nav-home">HOME</div>
  <div class="abs nav" style="left:206px;top:46px">ABOUT US</div>
  <div class="abs nav" style="left:309px;top:46px">OUR TEAM</div>
  <div class="abs nav" style="left:414px;top:46px">SERVICES</div>
  <div class="abs nav-line" style="left:182px;top:71px;width:300px"></div>

  <div class="abs nav" style="left:742px;top:46px">BLOG</div>
  <div class="abs nav" style="left:816px;top:46px">CONTACT US</div>
  <div class="abs nav" style="left:950px;top:46px;display:flex;align-items:center;gap:8px">
    <svg width="13" height="13" viewBox="0 0 24 24" aria-hidden="true"><path fill="#fff" d="M6.6 10.8a15.1 15.1 0 0 0 6.6 6.6l2.2-2.2a1 1 0 0 1 1-.25 11.4 11.4 0 0 0 3.6.57 1 1 0 0 1 1 1V20a1 1 0 0 1-1 1A17 17 0 0 1 3 4a1 1 0 0 1 1-1h3.5a1 1 0 0 1 1 1c0 1.25.2 2.45.57 3.57a1 1 0 0 1-.25 1z"/></svg>
    +1 (555) 010 0199
  </div>
  <div class="abs nav-line" style="left:735px;top:71px;width:353px"></div>

  <div class="abs brand" style="left:0;top:82px;width:1200px;justify-content:center;font-size:38px;letter-spacing:2px;line-height:1">
    <span class="brand-dot"></span>VINDMARK
  </div>

  <h1 class="abs hero-title">VINDMARK</h1>
  <p class="abs hero-text">Lorem ipsum dolor sit amet, consectetur adipiscing elit, sed do eiusmod tempor incididunt ut labore et dolore magna aliqua.Ut enim ad minim veniam, ris nisi quat.</p>
  <div class="abs btn" style="left:112px;top:517px;width:132px;height:48px">GET STARTED</div>
  <span class="abs dot" style="left:572px"></span>
  <span class="abs dot" style="left:596px;background:var(--blue-light)"></span>
  <span class="abs dot" style="left:617px"></span>

  <!-- about -->
  <svg class="abs" style="left:96px;top:822px" width="530" height="402" viewBox="0 0 530 402" role="img" aria-label="Black and white portrait of the practitioner">
    <defs>
      <radialGradient id="portraitTone" cx=".45" cy=".45" r=".7">
        <stop offset="0" stop-color="#cfcfcf"/><stop offset=".35" stop-color="#8a8a8a"/><stop offset=".7" stop-color="#4c4c4c"/><stop offset="1" stop-color="#2e2e2e"/>
      </radialGradient>
      <linearGradient id="portraitLight" x1="1" y1="0" x2="0" y2="1">
        <stop offset="0" stop-color="#ffffff" stop-opacity=".45"/><stop offset=".5" stop-color="#ffffff" stop-opacity="0"/>
      </linearGradient>
    </defs>
    <path fill="var(--green)" transform="translate(3,12)" d="M150 8 C210 -12 260 20 272 70 C300 20 360 28 420 62 C470 90 520 150 525 220 C528 260 500 280 450 285 C420 290 390 300 375 330 C355 380 300 405 250 395 C200 385 160 350 155 300 C110 300 50 300 15 270 C-5 245 0 175 50 150 C60 145 70 140 78 135 C75 90 100 25 150 8 Z"/>
    <path fill="url(#portraitTone)" d="M150 8 C210 -12 260 20 272 70 C300 20 360 28 420 62 C470 90 520 150 525 220 C528 260 500 280 450 285 C420 290 390 300 375 330 C355 380 300 405 250 395 C200 385 160 350 155 300 C110 300 50 300 15 270 C-5 245 0 175 50 150 C60 145 70 140 78 135 C75 90 100 25 150 8 Z"/>
    <path fill="url(#portraitLight)" d="M150 8 C210 -12 260 20 272 70 C300 20 360 28 420 62 C470 90 520 150 525 220 C528 260 500 280 450 285 C420 290 390 300 375 330 C355 380 300 405 250 395 C200 385 160 350 155 300 C110 300 50 300 15 270 C-5 245 0 175 50 150 C60 145 70 140 78 135 C75 90 100 25 150 8 Z"/>
  </svg>

  <h2 class="abs" style="left:697px;top:828px;font-size:35px;line-height:44px">
    <span class="h-strong">ABOUT</span> <span class="h-light">ME</span><span class="h-mark"></span>
  </h2>
  <p class="abs" style="left:694px;top:882px;font-family:'Poppins',sans-serif;font-size:26px;color:var(--green)">Dr Della M Quorne DACM, L.Ac.</p>
  <p class="abs body-text" style="left:697px;top:939px;width:398px">At a young age, I discovered the transformative power of Eastern Medicine when it helped me overcome lung concerns, propelling me toward my dreams as a young athlete. Years later, I faced a pivotal choice: How could I best serve and heal my community? The answer was crystal clear—Eastern Medicine. As an Eastern Medicine doctor, I’ve had the privilege of positively impacting my community through integrative health choices.</p>
  <div class="abs btn" style="left:697px;top:1167px;width:130px;height:48px">READ MORE</div>

  <!-- project -->
  <section class="abs project">
    <svg class="abs" style="left:0;top:0" width="1200" height="557" viewBox="0 0 1200 557" role="img" aria-label="Collage of diamond-shaped wellness photos with fruit, spa, remedies and meditation, among potted succulents">
      <defs>
        <radialGradient id="fruitTone" cx=".5" cy=".55" r=".6"><stop offset="0" stop-color="#d8763a"/><stop offset=".35" stop-color="#c4443a"/><stop offset=".7" stop-color="#8fb43e"/><stop offset="1" stop-color="#6e4a2e"/></radialGradient>
        <linearGradient id="spaTone" x1="0" y1="0" x2="1" y2="1"><stop offset="0" stop-color="#a8876a"/><stop offset=".5" stop-color="#d7c7b4"/><stop offset="1" stop-color="#f2ece4"/></linearGradient>
        <linearGradient id="roomTone" x1="0" y1="0" x2="1" y2="1"><stop offset="0" stop-color="#f0f0f0"/><stop offset=".55" stop-color="#c9d6e6"/><stop offset="1" stop-color="#8fb0d8"/></linearGradient>
        <linearGradient id="blocksTone" x1="0" y1="0" x2="1" y2="1"><stop offset="0" stop-color="#eadfcd"/><stop offset="1" stop-color="#c2915e"/></linearGradient>
        <linearGradient id="yogaTone" x1="0" y1="0" x2="1" y2="0"><stop offset="0" stop-color="#f6f6f6"/><stop offset=".6" stop-color="#e2e2e2"/><stop offset="1" stop-color="#3a3a3a"/></linearGradient>
        <radialGradient id="plantA" r=".55"><stop offset="0" stop-color="#a6d36a"/><stop offset=".55" stop-color="#4e8f45"/><stop offset="1" stop-color="#2c5a33" stop-opacity="0"/></radialGradient>
        <radialGradient id="plantB" r=".55"><stop offset="0" stop-color="#d2d98a"/><stop offset=".55" stop-color="#8f9a58"/><stop offset="1" stop-color="#6a6a3c" stop-opacity="0"/></radialGradient>
        <radialGradient id="plantC" r=".55"><stop offset="0" stop-color="#7a3b2e"/><stop offset=".35" stop-color="#4d7a3e"/><stop offset="1" stop-color="#3e6a35" stop-opacity="0"/></radialGradient>
      </defs>
      <polygon points="400,0 700,0 590,190" fill="url(#yogaTone)"/>
      <polygon points="805,24 1000,219 805,414 610,219" fill="url(#fruitTone)"/>
      <polygon points="840,0 1190,0 1015,175" fill="url(#spaTone)"/>
      <polygon points="1200,105 1200,330 1092,218" fill="url(#blocksTone)"/>
      <polygon points="1015,250 1200,435 1200,557 945,557 845,457" fill="url(#roomTone)"/>
      <ellipse cx="40" cy="90" rx="62" ry="62" fill="url(#plantA)"/>
      <ellipse cx="295" cy="45" rx="64" ry="64" fill="url(#plantA)"/>
      <ellipse cx="50" cy="505" rx="62" ry="62" fill="url(#plantB)"/>
      <ellipse cx="425" cy="497" rx="100" ry="70" fill="url(#plantC)"/>
      <ellipse cx="682" cy="440" rx="80" ry="72" fill="url(#plantA)"/>
    </svg>
  </section>

  <h2 class="abs" style="left:112px;top:1452px;font-size:35px;line-height:51px">
    <span class="h-strong">OUR LATEST</span><br><span class="h-light">PROJECT</span><span class="h-mark"></span>
  </h2>
  <p class="abs body-text" style="left:112px;top:1565px;width:488px">Lorem ipsum dolor sit amet, consectetur adipiscing elit, sed do eiusmod tempor incididunt ut labore et dolore magna aliqua. Ut enim ad minim veniam, quis nostrud exercitation ullamco laboris nisi ut aliquip ex ea commodo consequat. Duis aute irure dolor in reprehenderit in voluptate velit esse cillum dolore eu fugiat nulla pariatur.</p>
  <div class="abs btn" style="left:112px;top:1721px;width:130px;height:48px">VIEW MORE</div>

  <!-- newsletter -->
  <section class="abs newsletter" role="img" aria-label="Faint watercolour bamboo and flower backdrop"></section>
  <h2 class="abs" style="left:0;top:1955px;width:1200px;text-align:center;font-size:35px;line-height:50px">
    <span class="h-strong">SIGN UP FOR</span> <span class="h-light">NEWSLETTER</span><span class="h-mark"></span>
  </h2>
  <p class="abs body-text" style="left:300px;top:2036px;width:600px;text-align:center">Lorem ipsum dolor sit amet, consectetur adipiscing elit, sed do eiusmod tempor incididunt ut labore et dolore magna aliqua. Ut enim ad minim veniam, quis nostrud exercitation ullamco laboris nisi ut aliquip ex ea commodo consequat.</p>
  <div class="abs email">Enter your email</div>
  <div class="abs btn" style="left:535px;top:2238px;width:130px;height:48px">SEND</div>

  <!-- footer -->
  <footer class="abs footer"></footer>
  <div class="abs brand" style="left:112px;top:2540px;font-size:36px;letter-spacing:1px">
    <span class="brand-dot"></span>VINDMARK
  </div>
  <span class="abs social" style="left:112px" aria-label="Social profile"><span class="social-dot"></span></span>
  <span class="abs social" style="left:180px" aria-label="Social profile"><span class="social-dot"></span></span>

  <h3 class="abs f-head" style="left:370px;top:2476px">VISIT US</h3>
  <span class="abs f-rule" style="left:370px;top:2509px"></span>
  <svg class="abs" style="left:369px;top:2538px" width="16" height="20" viewBox="0 0 24 30" aria-hidden="true"><path fill="var(--blue-light)" d="M12 0a11 11 0 0 0-11 11c0 8 11 19 11 19s11-11 11-19A11 11 0 0 0 12 0zm0 15a4 4 0 1 1 0-8 4 4 0 0 1 0 8z"/></svg>
  <p class="abs f-text" style="left:403px;top:2528px">Vindmark<br>Address Comes Here.</p>

  <h3 class="abs f-head" style="left:662px;top:2476px">CONTACT US</h3>
  <span class="abs f-rule" style="left:662px;top:2509px;width:82px"></span>
  <svg class="abs" style="left:664px;top:2535px" width="17" height="17" viewBox="0 0 24 24" aria-hidden="true"><path fill="var(--blue-light)" d="M6.6 10.8a15.1 15.1 0 0 0 6.6 6.6l2.2-2.2a1 1 0 0 1 1-.25 11.4 11.4 0 0 0 3.6.57 1 1 0 0 1 1 1V20a1 1 0 0 1-1 1A17 17 0 0 1 3 4a1 1 0 0 1 1-1h3.5a1 1 0 0 1 1 1c0 1.25.2 2.45.57 3.57a1 1 0 0 1-.25 1z"/></svg>
  <svg class="abs" style="left:664px;top:2574px" width="18" height="13" viewBox="0 0 24 17" aria-hidden="true"><path fill="var(--blue-light)" d="M0 0h24v17H0z"/><path fill="none" stroke="#061a1c" stroke-width="2" d="M1 1l11 8 11-8"/></svg>
  <p class="abs f-text" style="left:698px;top:2528px">+1 (555) 010 0199<br><span style="display:inline-block;margin-top:8px">info@vindmark.example</span></p>

  <h3 class="abs f-head" style="left:982px;top:2476px">QUICK LINKS</h3>
  <span class="abs f-rule" style="left:982px;top:2509px;width:82px"></span>
  <ul class="abs quick f-text" style="left:982px;top:2528px">
    <li>Home</li><li>About us</li><li>Our Team</li><li>Services</li><li>Blog</li><li>Contact Us</li>
  </ul>

  <span class="abs" style="left:377px;top:2642px;width:557px;height:1px;background:rgba(255,255,255,.7)"></span>
  <p class="abs f-text" style="left:370px;top:2672px;font-size:17px">2024 Vindmark. All Rights Reserved.</p>
</div>
</body>
</html>
```